Need Eye Catching For Sale By Owner Signs

In need of a Eye Catching For Sale By Owner Sign design. I plan on using the sign to market buildings and raw land that I own. The design should be able to scale to different rectangular dimensions for example a yard stake sign or a large 4' x 6' sign to be tacked to plywood. The design should have a dead space near the bottom that I can insert more detail information into at a later time.

The main tag line "For Sale By Owner" and the contact number "319-562-4097" needs to be easily be read from a distance.

```html
<!DOCTYPE html>
<html lang="en">
<head>
<meta charset="utf-8">
<title>For Sale By Owner Sign</title>
<link rel="stylesheet" href="https://fonts.googleapis.com/css2?family=Anton&display=swap">
<style>
  :root {
    --sign-red: #fd3914;
    --sign-red-light: #ff5a38;
    --sign-white: #ffffff;
  }
  html, body {
    margin: 0;
    padding: 0;
    width: 1200px;
    height: 798px;
    overflow: hidden;
  }
  .sign {
    position: relative;
    width: 1200px;
    height: 798px;
    background: var(--sign-red);
    overflow: hidden;
    font-family: "Anton", "Oswald", Impact, sans-serif;
  }
  .houses-art {
    position: absolute;
    left: 30px;
    top: 24px;
    width: 280px;
    height: 256px;
    background: linear-gradient(160deg, rgba(255,255,255,0.55), rgba(255,255,255,0.2));
    border-radius: 4px;
  }
  .headline-top {
    position: absolute;
    left: 358px;
    top: 42px;
    margin: 0;
    color: var(--sign-white);
    font-size: 212px;
    line-height: 1;
    letter-spacing: 10px;
    font-weight: 400;
    white-space: nowrap;
  }
  .divider {
    position: absolute;
    left: 0;
    width: 1200px;
    height: 8px;
    background: var(--sign-white);
  }
  .divider--upper { top: 289px; }
  .divider--lower { top: 588px; }
  .owner-band {
    position: absolute;
    left: 0;
    top: 305px;
    width: 1200px;
    height: 185px;
    background: var(--sign-white);
  }
  .headline-bottom {
    position: absolute;
    left: 80px;
    top: 309px;
    margin: 0;
    color: var(--sign-red);
    font-size: 173px;
    line-height: 1;
    letter-spacing: 8px;
    font-weight: 400;
    white-space: nowrap;
  }
  .phone {
    position: absolute;
    left: 190px;
    top: 500px;
    margin: 0;
    color: var(--sign-white);
    font-size: 73px;
    line-height: 1;
    letter-spacing: 6px;
    font-weight: 400;
    white-space: nowrap;
  }
  .skyline-art {
    position: absolute;
    left: 850px;
    top: 305px;
    width: 350px;
    height: 255px;
    background: linear-gradient(180deg, var(--sign-red-light), var(--sign-red));
  }
  .details-panel {
    position: absolute;
    left: 32px;
    top: 622px;
    width: 1134px;
    height: 154px;
    background: var(--sign-white);
    border-radius: 24px;
  }
</style>
</head>
<body>
  <main class="sign">
    <div class="houses-art" role="img" aria-label="White line drawing of a cluster of houses with windows"></div>
    <h1 class="headline-top">FOR SALE</h1>
    <div class="divider divider--upper"></div>
    <div class="owner-band"></div>
    <div class="skyline-art" role="img" aria-label="Red silhouette of a city skyline with lit windows"></div>
    <p class="headline-bottom">BY OWNER</p>
    <p class="phone">319-562-4097</p>
    <div class="divider divider--lower"></div>
    <div class="details-panel" aria-label="Space for property details"></div>
  </main>
</body>
</html>
```